London Based Property Finding Company - have logo already

We find property for private purchasers and investors in London, UK.  We work for the BUYER, whereas estate agencies/real estate companies work for the seller. We offer a much more personalised service to UK and overseas purchasers.

We would like the following:

*A double sided business card

*A letterhead

We have attached two versions of the logo. Each logo style is set on two different coloured backgrounds. Please choose one of the two designs, whichever you prefer or feel more comfortable with, and produce one in black and one in white background.

This applies to both pieces of stationery.

THE BUSINESS CARD:

We would like the company name placed on its own on one side of the card and the contact details and what we do on the other.

e.g.

SIDE 1:

BRAMWELL PROPERTY FINDERS

SIDE 2:

Owen Bramwell

t: 0208 394 2261

m: +44(0)7940 318 472

e: info@bramwellpropertyfinders.co.uk

w: bramwellpropertyfinders.co.uk

London Property Finders and Search Agents

I will leave the layout up to you, but a minimalist layout is preferred. If you would like to put additional detial or design on the card then that is up to, but not specified.

It is optional to have the company name on side 2, but if you do use it, please make it smaller. than on the 1st side.

The design needs to be simple, professional and not too in your face.

If you are using the black background design on side 1 for the logo, then maybe a white backgounnd can be used on side 2 with a black typeface.

The type face for the contacts details should be sans serif standard typeface. Please experiment with the desciprtion.

-

THE LETTERHEAD;

You can experiment with the layout for the letterhead. e.g logo centre aligned on the top of the page with the contact details and address at the bottom of the page OR the logo, description running along a bar on the top of the page with the contact details and website address at the bottom. Please try and experiment with this, but the less 'busy', the better.

Here is info that needs to be on the letterhead.

Bramwell Property Finders

t: 0208 394 2261

m: +44(0)7940 318 472

(PLEASE NOTE; the below company info must be placed at the bottom of the page as a footer, in small text.)

Pemberly Holdings Ltd Trading as Bramwell Property Finders, a company registered in England & Wales, No.5917302 , Registered office is 41 Kelmscott House, Ashdown Lane, London, SW9 7QJ, t: 0208 394 2261, m: +44(0)7940 318 472, e: info@bramwellpropertyfinders.co.uk

Best of luck!

Thank you

Dear Designer,

I have now attached the supporting files to this brief.

Thanks,

Owen Bramwell
Bramwell Property Finders

```html
<!DOCTYPE html>
<html lang="en">
<head>
<meta charset="utf-8">
<title>Bramwell Property Finders — Stationery</title>
<link rel="stylesheet" href="https://fonts.googleapis.com/css2?family=Questrial&display=swap">
<style>
  :root {
    --ink: #0d0d0d;
    --paper: #ffffff;
    --accent: #7cc8ec;
    --text-dark: #1a1a1a;
    --text-light: #f2f2f2;
    --shadow: 0 2px 6px rgba(0,0,0,0.28);
  }
  * { margin: 0; padding: 0; box-sizing: border-box; }
  html, body { width: 1200px; height: 1004px; overflow: hidden; background: var(--paper); }
  body { position: relative; font-family: "Questrial", "Century Gothic", sans-serif; color: var(--text-dark); }

  .wordmark { font-family: "Questrial", sans-serif; color: var(--text-light); letter-spacing: 0.05em; white-space: nowrap; font-weight: 400; }

  /* Letterhead */
  .letterhead { position: absolute; left: 260px; top: 64px; width: 650px; height: 841px; background: var(--paper); box-shadow: var(--shadow); }
  .letterhead__bar { position: absolute; left: 0; top: 0; width: 100%; height: 117px; background: var(--ink); border-bottom: 4px solid var(--accent); }
  .letterhead__bar .wordmark { position: absolute; left: 34px; top: 44px; font-size: 19px; }
  .letterhead__contact { position: absolute; right: 34px; top: 38px; text-align: right; font-size: 10px; line-height: 18.5px; color: var(--text-light); }
  .letterhead__contact .web { color: var(--accent); }
  .letterhead__footer { position: absolute; left: 0; bottom: 14px; width: 100%; text-align: center; font-size: 8.5px; line-height: 15.5px; color: var(--text-dark); }

  /* Cards */
  .card { position: absolute; box-shadow: var(--shadow); overflow: hidden; }
  .card--landscape { width: 270px; height: 166px; }
  .card--portrait { width: 174px; height: 270px; }

  .card--black-front { left: 154px; top: 351px; background: var(--ink); transform: rotate(-20deg); }
  .card--black-front .wordmark { position: absolute; left: 0; width: 100%; text-align: center; top: 84px; font-size: 11px; }

  .card--white-back { left: 282px; top: 464px; width: 307px; height: 175px; background: var(--paper); transform: rotate(-9deg); }
  .card__band { position: absolute; left: 0; width: 100%; background: var(--ink); }
  .card--white-back .card__band { top: 34px; height: 40px; }
  .card--white-back .wordmark { position: absolute; right: 18px; top: 14px; font-size: 10px; }
  .card--white-back .details { position: absolute; left: 14px; top: 96px; }

  .details__name { font-size: 14px; margin-bottom: 3px; }
  .details__line { font-size: 8.5px; line-height: 11.5px; white-space: nowrap; }
  .details__line b { display: inline-block; width: 14px; font-weight: 400; }

  .card--portrait-logo { left: 697px; top: 276px; background: var(--paper); transform: rotate(12deg); }
  .card--portrait-logo .card__band { top: 100px; height: 46px; }
  .card--portrait-logo .wordmark { position: absolute; left: 0; width: 100%; text-align: center; top: 18px; font-size: 8px; }

  .card--portrait-details { left: 707px; top: 499px; background: var(--paper); transform: rotate(-14deg); }
  .card--portrait-details .card__band { top: 105px; height: 98px; }
  .card--portrait-details .details { position: absolute; left: 12px; top: 14px; color: var(--text-light); }
  .card--portrait-details .details__name { color: var(--accent); font-size: 13px; }
  .card--portrait-details .details__line { font-size: 7.5px; line-height: 10.5px; }
</style>
</head>
<body>

<section class="letterhead">
  <header class="letterhead__bar">
    <span class="wordmark">BRAMWELL PROPERTY FINDERS</span>
    <div class="letterhead__contact">
      <div>0208 394 2261</div>
      <div>+44(0)7940 318 472</div>
      <div>info@bramwellpropertyfinders.co.uk</div>
      <div class="web">bramwellpropertyfinders.co.uk</div>
    </div>
  </header>
  <footer class="letterhead__footer">
    <div>Pemberly Holdings Ltd Trading as Bramwell Property Finders, a company registered in England &amp; Wales, No.5917302 ,</div>
    <div>Registered office is 41 Kelmscott House, Ashdown Lane, London, SW9 7QJ,</div>
    <div>t: 0208 394 2261, m: +44(0)7940 318 472, e: info@bramwellpropertyfinders.co.uk</div>
  </footer>
</section>

<div class="card card--landscape card--black-front">
  <span class="wordmark">BRAMWELL PROPERTY FINDERS</span>
</div>

<div class="card card--white-back">
  <div class="card__band"><span class="wordmark">BRAMWELL PROPERTY FINDERS</span></div>
  <div class="details">
    <div class="details__name">owen bramwell</div>
    <div class="details__line"><b>t:</b>0208 394 2261</div>
    <div class="details__line"><b>m:</b>+44(0)7940 318 472</div>
    <div class="details__line"><b>e:</b>info@bramwellpropertyfinders.co.uk</div>
    <div class="details__line"><b>w:</b>bramwellpropertyfinders.co.uk</div>
  </div>
</div>

<div class="card card--portrait card--portrait-logo">
  <div class="card__band"><span class="wordmark">BRAMWELL PROPERTY FINDERS</span></div>
</div>

<div class="card card--portrait card--portrait-details">
  <div class="card__band">
    <div class="details">
      <div class="details__name">owen bramwell</div>
      <div class="details__line"><b>t:</b>0208 394 2261</div>
      <div class="details__line"><b>m:</b>+44(0)7940 318 472</div>
      <div class="details__line"><b>e:</b>info@bramwellpropertyfinders.co.uk</div>
      <div class="details__line"><b>w:</b>bramwellpropertyfinders.co.uk</div>
    </div>
  </div>
</div>

</body>
</html>
```